Graphic Design Project - Coffee Label

I am a coffee roasting business and I need a professional label design for my bag of coffee. this needs to be in a format that we can change the "title" or "weight" of the product frequently ourselves. We do have photoshop, but cannot create the project, but can edit if need be to print. Our labels are 3"x8". we will want the colors to bleed to the end. The labels are white and glossy, but i want the design to give the illusion that the color of the label is not evident. I have a logo. I do not want the design to have a border. Since the label is only 3" wide and 8" tall the design needs to be creative to look good. although coffee colors are ok, I want a lot more color to not be boring. We could frequently change the label size and would need to adjust accordingly from the current design.
Updates

Reason: I just decided to remove my refundable contract into committed payment to a designer. I would like a few more days to broadcast that option.

Target Market(s)

30-50 year olds that have money and want to buy quality

Industry/Entity Type

Business

Requirements
Must have
• we currently are using label 3" wide and 8" tall. First and foremost I need to be able to edit the words on the label. I will need to change the net wt and the coffee blend names. I would like the ability to change the size if need be. the company name is
1. Heron Ridge Coffee
2. Artisan Coffee Roasting
3. Needs to be a large space for a particular coffee name i.e Rain, Fern and Ember Blend. Use this blend, but I need to be able to edit it for other blends.
4. Under the blend it should say Whole Bean. Also need to be able to edit.
5. At the bottom it should say Roasted in Fernhollow, Avalo. www.heronridgecoffee.example
6. Below the coffee name there should be Net Weight ie 16 oz (this also needs to be editable for us)
Nice to have
• I have a logo, but it can be different. Labels are white, but I don't want borders, and would like the colors to bleed and not to appear to be a white label. the bags are light grey/silver metallic. Although many use a lot of "coffee" colors for design, I do not. I have pics of coffee beans; it doesn't have to be used. I don't want to be just a block of a pic of beans. Other pics of coffee related ideas is fine with me. I don't need the brand to dominate the label. Bolder colors. I have attached roasting pics. These do not have to be used, but can. If used please edit out the extraneous background.
Should not have
• Do not use borders. I want the colors to bleed to the end. I don't want the white label to show through as though I have a typed page of print. I don't want just coffee colors used. I don't want light colors. I don't want a "square" looking format wherein everything is just line by line. Asymmetrical is ok.

```html
<!DOCTYPE html>
<html lang="en">
<head>
<meta charset="utf-8">
<title>Heron Ridge Coffee – Rain, Fern and Ember Blend Label</title>
<link rel="stylesheet" href="https://fonts.googleapis.com/css2?family=Cinzel:wght@400;500;600&family=Crimson+Text:ital,wght@1,400;1,700&display=swap">
<style>
  :root {
    --canvas: #ffffff;
    --label-orange: #c53d12;
    --ink: #0b0806;
    --ink-soft: #4a3a33;
    --sage-band: #7e8a6f;
    --bean-dark: #2a1a12;
    --bean-mid: #5a3522;
    --bean-light: #7a4a30;
  }
  * { margin: 0; padding: 0; box-sizing: border-box; }
  html, body {
    width: 1200px; height: 1000px; overflow: hidden;
    background: var(--canvas);
  }
  .canvas { position: relative; width: 1200px; height: 1000px; }
  .label {
    position: absolute; left: 420px; top: 20px;
    width: 360px; height: 960px;
    background: var(--label-orange);
    color: var(--ink);
    overflow: hidden;
  }
  .brand-disc { position: absolute; left: 68px; top: 17px; }
  .brand-name {
    position: absolute; left: 0; top: 282px; width: 360px;
    font-family: "Cinzel", serif; font-weight: 500;
    font-size: 70px; line-height: 72px;
    text-align: center; letter-spacing: 1px;
  }
  .tagline {
    position: absolute; left: 0; top: 494px; width: 360px;
    text-align: center;
    font-family: "Crimson Text", serif; font-style: italic;
    font-size: 28px; line-height: 32px; color: var(--ink-soft);
  }
  .blend-name {
    position: absolute; left: 22px; top: 550px; width: 320px;
    font-family: "Crimson Text", serif; font-style: italic; font-weight: 700;
    font-size: 40px; line-height: 47px;
  }
  .blend-name .line-two { display: block; text-align: right; }
  .product-spec {
    position: absolute; left: 0; top: 652px; width: 360px;
    display: flex; justify-content: center; align-items: baseline;
    font-family: "Cinzel", serif; font-weight: 500; white-space: nowrap;
  }
  .product-spec .grind { font-size: 30px; margin-right: 16px; }
  .product-spec .weight { font-size: 44px; }
  .sage-band {
    position: absolute; left: 0; width: 360px; height: 10px;
    background: var(--sage-band);
  }
  .sage-band.top { top: 708px; }
  .sage-band.bottom { top: 856px; }
  .bean-photo {
    position: absolute; left: 0; top: 718px; width: 360px; height: 138px;
    background: radial-gradient(circle at 30% 40%, var(--bean-light), transparent 55%),
                radial-gradient(circle at 75% 65%, var(--bean-mid), transparent 60%),
                var(--bean-dark);
  }
  .origin {
    position: absolute; left: 0; top: 878px; width: 360px;
    display: flex; justify-content: center; align-items: flex-end;
    font-family: "Cinzel", serif; white-space: nowrap;
  }
  .origin .city-block { display: flex; flex-direction: column; align-items: flex-end; }
  .origin .roasted-in { font-size: 17px; line-height: 16px; font-weight: 500; }
  .origin .city { font-size: 27px; line-height: 28px; font-weight: 600; }
  .origin .state { font-size: 40px; line-height: 38px; font-weight: 500; margin-left: 4px; }
  .web-address {
    position: absolute; left: 0; top: 925px; width: 360px; text-align: center;
    font-family: "Crimson Text", serif; font-style: italic;
    font-size: 21px; color: var(--ink-soft);
  }
</style>
</head>
<body>
<main class="canvas">
  <section class="label">
    <svg class="brand-disc" width="244" height="244" viewBox="0 0 244 244" aria-hidden="true">
      <circle cx="122" cy="122" r="122" fill="var(--ink)"/>
    </svg>

    <h1 class="brand-name">Heron<br>Ridge<br>Coffee</h1>
    <p class="tagline">Artisan Coffee Roasting</p>

    <h2 class="blend-name">Rain, Fern and<span class="line-two">Ember Blend</span></h2>

    <p class="product-spec"><span class="grind">Whole Bean</span><span class="weight">16oz</span></p>

    <div class="sage-band top"></div>
    <div class="bean-photo" role="img" aria-label="Photograph of dark roasted whole coffee beans"></div>
    <div class="sage-band bottom"></div>

    <p class="origin">
      <span class="city-block">
        <span class="roasted-in">Roasted in</span>
        <span class="city">Fernhollow</span>
      </span>
      <span class="state">Avalo</span>
    </p>
    <p class="web-address">www.heronridgecoffee.example</p>
  </section>
</main>
</body>
</html>
```